New business card design needed for Trucking/Staffing company!

I am looking for a business card design. The business name is Harbor Lane Freightworks, LLC. This company is a staffing company for commercial drivers/truck drivers. Most of our customers are trucking/supply companies. Our colors are blue/black/white/grey. The info I have on my current business cards is
-Spot for a name
-2 lines for an address
-3 lines for Office, cell, and fax
-email
-website(currently on backside of card with logo but can go anywhere)
Updates

Project Deadline Extended
Reason: Open to more designs

Target Market(s)

Trucking companies, building supply companies

Industry/Entity Type

Business

Contact Information for Business Card

Edgy but professional

Font styles to use
Other font styles liked:
• Open to suggestions

Colors
0555a3
000000
ffffff
9d9d9d

Requirements
Must have
• Must have the logo incorporated

```html
<!DOCTYPE html>
<html lang="en">
<head>
<meta charset="utf-8">
<title>Harbor Lane Freightworks, LLC — Business Card</title>
<link rel="stylesheet" href="https://fonts.googleapis.com/css2?family=EB+Garamond:wght@400;500;600&display=swap">
<style>
  :root {
    --brand-blue: #0b57a6;
    --ink: #111111;
    --paper: #ffffff;
    --backdrop: #d6d6d6;
    --card-shadow: rgba(0, 0, 0, 0.28);
  }
  * { box-sizing: border-box; margin: 0; padding: 0; }
  html, body {
    width: 1200px; height: 800px; overflow: hidden;
    background: var(--backdrop);
    font-family: "EB Garamond", Garamond, serif;
  }
  .canvas {
    position: relative; width: 1200px; height: 800px;
    display: flex; align-items: center; justify-content: center; gap: 50px;
  }
  .card {
    position: relative; width: 520px; height: 300px;
    border-radius: 22px; overflow: hidden;
    background: var(--paper);
    box-shadow: 0 10px 24px var(--card-shadow);
  }

  /* Back of card */
  .card--back { background: var(--brand-blue); }
  .card--back .band {
    position: absolute; left: 0; right: 0; top: 168px; height: 74px;
    background: var(--paper);
  }
  .card--back .brand-name {
    position: absolute; left: 0; right: 0; top: 58px;
    display: flex; align-items: center; justify-content: center; gap: 12px;
    color: var(--paper); font-size: 34px; font-weight: 600; letter-spacing: 0.5px;
  }
  .card--back .brand-name .brand-square {
    width: 22px; height: 22px; background: var(--paper);
  }
  .card--back .website {
    position: absolute; left: 0; right: 0; top: 186px;
    text-align: center; color: var(--brand-blue);
    font-size: 31px; font-weight: 500;
  }

  /* Front of card */
  .card--front .top-band {
    position: absolute; left: 0; right: 0; top: 0; height: 86px;
    background: var(--brand-blue);
  }
  .card--front .bottom-band {
    position: absolute; left: 0; right: 0; bottom: 0; height: 40px;
    background: var(--brand-blue);
  }
  .card--front .brand-name {
    position: absolute; right: 26px; top: 26px;
    display: flex; align-items: center; gap: 10px;
    color: var(--paper); font-size: 25px; font-weight: 600;
  }
  .card--front .brand-name .brand-square {
    width: 16px; height: 16px; background: var(--paper);
  }
  .holder {
    position: absolute; left: 28px; top: 118px; width: 190px; text-align: center;
  }
  .holder .holder-name {
    color: var(--brand-blue); font-size: 29px; font-weight: 600;
    font-variant: small-caps; letter-spacing: 0.5px; line-height: 1;
  }
  .holder .holder-position {
    display: flex; align-items: center; justify-content: center; gap: 6px;
    margin-top: 6px; color: var(--ink);
    font-size: 16px; letter-spacing: 1.5px; text-transform: uppercase;
  }
  .holder .holder-position::before,
  .holder .holder-position::after {
    content: ""; height: 2px; width: 34px; background: var(--ink);
  }
  .holder .holder-position::before { clip-path: polygon(0 50%, 100% 0, 100% 100%); }
  .holder .holder-position::after { clip-path: polygon(0 0, 100% 50%, 0 100%); }
  .divider {
    position: absolute; left: 236px; top: 104px; width: 2px; height: 128px;
    background: var(--ink);
  }
  .contact-list {
    position: absolute; left: 256px; top: 100px; list-style: none;
    color: var(--ink); font-size: 17px; line-height: 1.15;
  }
  .contact-list li {
    display: flex; align-items: flex-start; gap: 8px; margin-bottom: 5px;
  }
  .contact-list .icon {
    flex: none; width: 19px; height: 19px; border-radius: 4px;
    background: var(--brand-blue);
    display: flex; align-items: center; justify-content: center;
  }
  .contact-list .icon svg { width: 13px; height: 13px; fill: var(--paper); }
  .contact-list .icon--pin { border-radius: 50%; }
</style>
</head>
<body>
<main class="canvas">

  <section class="card card--back" aria-label="Back of business card">
    <div class="band"></div>
    <div class="brand-name"><span class="brand-square"></span>Harbor Lane Freightworks, LLC</div>
    <div class="website">www.harborlanefreight.com</div>
  </section>

  <section class="card card--front" aria-label="Front of business card">
    <div class="top-band"></div>
    <div class="bottom-band"></div>
    <div class="brand-name"><span class="brand-square"></span>Harbor Lane Freightworks, LLC</div>

    <div class="holder">
      <div class="holder-name">Name Here</div>
      <div class="holder-position">Position</div>
    </div>

    <div class="divider"></div>

    <ul class="contact-list">
      <li>
        <span class="icon" aria-label="Office phone">
          <svg viewBox="0 0 24 24"><path d="M6.6 10.8a15.1 15.1 0 0 0 6.6 6.6l2.2-2.2a1 1 0 0 1 1-.25 11.4 11.4 0 0 0 3.6.57 1 1 0 0 1 1 1V20a1 1 0 0 1-1 1A17 17 0 0 1 3 4a1 1 0 0 1 1-1h3.5a1 1 0 0 1 1 1 11.4 11.4 0 0 0 .57 3.6 1 1 0 0 1-.25 1z"/></svg>
        </span>123.456.789
      </li>
      <li>
        <span class="icon" aria-label="Cell phone">
          <svg viewBox="0 0 24 24"><path d="M7 2h10a1 1 0 0 1 1 1v18a1 1 0 0 1-1 1H7a1 1 0 0 1-1-1V3a1 1 0 0 1 1-1zm1 3v13h8V5zm4 14.2a1 1 0 1 0 0 2 1 1 0 0 0 0-2z"/></svg>
        </span>123.456.789
      </li>
      <li>
        <span class="icon" aria-label="Fax">
          <svg viewBox="0 0 24 24"><path d="M7 2h10v5H7zM4 8h16a2 2 0 0 1 2 2v7h-4v5H6v-5H2v-7a2 2 0 0 1 2-2zm4 8v4h8v-4z"/></svg>
        </span>123.456.789
      </li>
      <li>
        <span class="icon" aria-label="Email">
          <svg viewBox="0 0 24 24"><path d="M2 5h20v14H2zm2 2v.5l8 5 8-5V7zm0 2.9V17h16V9.9l-8 5z"/></svg>
        </span>name@harborlanefreight.com
      </li>
      <li>
        <span class="icon icon--pin" aria-label="Address">
          <svg viewBox="0 0 24 24"><path d="M12 2a7 7 0 0 1 7 7c0 5-7 13-7 13S5 14 5 9a7 7 0 0 1 7-7zm0 4.5a2.5 2.5 0 1 0 0 5 2.5 2.5 0 0 0 0-5z"/></svg>
        </span>Address Line 1<br>Address Line 2
      </li>
    </ul>
  </section>

</main>
</body>
</html>
```